Baby Shower Invitation for Vectored Image Provided

Caroline & Desmond's Baby Shower - Black/White/Gold Colors preferred
Please use the vectored portrait image attached. I'd like us on the lower right side of the invitation.
Can be horizontal or vertical layout.
The second image attached has the information needed for you to complete.
I don't want that style copied, it is just an example.

```html
<!DOCTYPE html>
<html lang="en">
<head>
<meta charset="utf-8">
<title>A Little Man Baby Shower</title>
<link href="https://fonts.googleapis.com/css2?family=Cinzel:wght@600;700&family=Great+Vibes&family=Montserrat:wght@500;600&display=swap" rel="stylesheet">
<style>
  :root {
    --black: #0c0c0c;
    --black-soft: #1a1a1a;
    --white: #ffffff;
    --gold-light: #f3dc8a;
    --gold: #d4af37;
    --gold-dark: #9b7b22;
  }
  html, body {
    margin: 0;
    padding: 0;
    overflow: hidden;
    background: var(--black);
  }
  .invitation {
    position: relative;
    width: 1200px;
    height: 1200px;
    overflow: hidden;
    background: radial-gradient(circle at 30% 25%, var(--black-soft) 0%, var(--black) 70%);
  }
  .frame {
    position: absolute;
    inset: 40px;
    border: 4px solid var(--gold);
  }
  .frame--inner {
    inset: 58px;
    border: 1px solid var(--gold-dark);
  }
  .headline {
    position: absolute;
    left: 0;
    width: 1200px;
    margin: 0;
    text-align: center;
  }
  .headline--kicker {
    top: 100px;
    font-family: "Great Vibes", cursive;
    font-weight: 400;
    font-size: 96px;
    line-height: 1.2;
    color: var(--gold-light);
  }
  .headline--title {
    top: 230px;
    font-family: "Cinzel", serif;
    font-weight: 700;
    font-size: 88px;
    line-height: 1.1;
    letter-spacing: 8px;
    color: var(--white);
  }
  .divider {
    position: absolute;
    height: 2px;
    background: linear-gradient(90deg, transparent, var(--gold), transparent);
  }
  .divider--top { left: 250px; width: 700px; top: 370px; }
  .divider--details { left: 140px; width: 460px; top: 720px; }
  .details {
    position: absolute;
    left: 100px;
    width: 540px;
    margin: 0;
    text-align: center;
  }
  .details--honoring {
    top: 450px;
    font-family: "Montserrat", sans-serif;
    font-weight: 600;
    font-size: 24px;
    letter-spacing: 8px;
    color: var(--gold);
  }
  .details--names {
    top: 500px;
    font-family: "Great Vibes", cursive;
    font-weight: 400;
    font-size: 84px;
    line-height: 1.1;
    color: var(--white);
  }
  .details--date {
    top: 770px;
    font-family: "Cinzel", serif;
    font-weight: 600;
    font-size: 44px;
    letter-spacing: 4px;
    color: var(--white);
  }
  .details--time {
    top: 845px;
    font-family: "Montserrat", sans-serif;
    font-weight: 500;
    font-size: 20px;
    letter-spacing: 3px;
    color: var(--gold-light);
  }
  .details--place {
    top: 910px;
    font-family: "Montserrat", sans-serif;
    font-weight: 500;
    font-size: 20px;
    line-height: 1.6;
    letter-spacing: 3px;
    color: var(--gold-light);
  }
  .portrait-arch {
    position: absolute;
    left: 690px;
    top: 430px;
    width: 400px;
    height: 710px;
    border: 3px solid var(--gold);
    border-bottom: none;
    border-radius: 200px 200px 0 0;
    box-sizing: border-box;
  }
  .couple-art {
    position: absolute;
    left: 760px;
    top: 490px;
    width: 260px;
    height: 650px;
    border-radius: 110px 110px 0 0;
    background: linear-gradient(90deg, #11d3f0 0%, #37c3d2 45%, #69d1c2 75%, #b8a3b5 100%);
  }
</style>
</head>
<body>
  <main class="invitation">
    <div class="frame"></div>
    <div class="frame frame--inner"></div>

    <p class="headline headline--kicker">A Little Man</p>
    <h1 class="headline headline--title">BABY SHOWER</h1>
    <div class="divider divider--top"></div>

    <p class="details details--honoring">HONORING</p>
    <p class="details details--names">Caroline &amp;<br>Desmond</p>
    <div class="divider divider--details"></div>
    <p class="details details--date">08.10.2020</p>
    <p class="details details--time">SIX O'CLOCK IN THE AFTERNOON</p>
    <p class="details details--place">1243 STREET NAME HERE,<br>YOUR CITY</p>

    <div class="portrait-arch"></div>
    <div class="couple-art" role="img" aria-label="Vector portrait of Caroline and Desmond, the expecting couple, standing together"></div>
  </main>
</body>
</html>
```